Hollowbrook Yard Services - Needs a business card! Easy JOB!

I need a business card for a new company called Hollowbrook Yard Services. I will be offering the below services.

I am relatively open for ideas, so please be at your creative best.

I think I will list all the services offered on the rear of the card.

- Gardening
- Lawn Care
- Hedge Trimming
- Rubbish Removal
- Weeding/Spraying
- Landscaping
- Gutter Cleaning
- Solar Panel Cleaning
- Irrigation
- Pruning
- On-Site Mulching
- Ask for other services

I am still a little undecided on the colours. I prefer the logos with the Blue text, but I am open for ideas ( the logo/texts colours are not final).

Please use the catch phrase "What can Hollowbrook do for you?"

Here are the required details.

Hollowbrook Yard Services

Miles Fenwarick (owner)
Ph: 1300 555 014
Mob: 0400 555 286

miles@hollowbrookyard.com.au
www.hollowbrookyard.com.au
facebook.com/HollowbrookYard
twitter.com/HollowbrookYard
ABN: 555 019 472 ( this can be in smaller text somewhere, this is the least important )

Thankyou in advance! And good luck.

regards,
Miles
Updates

Hi everyone, please make sure you include the phrase "What can Hollowbrook do for you?" on the designs.

thanks,
Miles

Definitely liking the focus on a majority of the design on the blue colour from the logo. Also a splash of green in the plant.

Please make sure you list the services provided on the rear of the card. thanks.

With the service listing, please make "ask for other services" stand out, either a different colour or position or size... as long as it is more noticeable than the other services listed. Thanks.

Industry/Entity Type

Business

Requirements
Must have
• - use the font supplied (Brandon Family Font)
- use of the catch phrase "What can Hollowbrook do for you?"
- Double sided design
- Chatterly and Quipster logos/links
- Please use symbol/picture for "phone" "mobile" "email" instead of using the words.
- List the services provided on the rear of the card

```html
<!DOCTYPE html>
<html lang="en">
<head>
<meta charset="utf-8">
<title>Hollowbrook Yard Services – Business Card</title>
<link rel="stylesheet" href="https://fonts.googleapis.com/css2?family=Jost:wght@500;600;700&family=Quicksand:wght@700&display=swap">
<style>
  :root {
    --backdrop: #d9d6d0;
    --card-black: #0b0c0b;
    --stripe-dark: #1b1c1c;
    --stripe-mid: #2a2b2b;
    --leaf-green: #7cc943;
    --bright-green: #5fe04a;
    --lemon: #e6ea1f;
    --rule-green: #49d35a;
    --rule-yellow: #dfe526;
  }
  * { margin: 0; padding: 0; box-sizing: border-box; }
  html, body {
    width: 1200px; height: 900px; overflow: hidden;
    background: var(--backdrop);
  }
  .sheet {
    position: relative; width: 1200px; height: 900px;
  }
  .card {
    position: absolute; left: 220px; width: 760px; height: 400px;
    border-radius: 30px; overflow: hidden;
    background: linear-gradient(180deg, var(--stripe-mid), var(--stripe-dark));
    box-shadow: 0 6px 18px rgba(0,0,0,.35);
  }
  .card--front { top: 30px; }
  .card--back { top: 470px; }

  .card__band {
    position: absolute; left: 0; right: 0; top: 104px; height: 188px;
    background: linear-gradient(180deg, #050605 0%, var(--card-black) 50%, #141613 100%);
    border-top: 2px solid var(--rule-green);
    border-bottom: 2px solid var(--rule-yellow);
    box-shadow: 0 -10px 18px -8px rgba(73,211,90,.45), 0 10px 18px -8px rgba(223,229,38,.45);
  }

  .tagline {
    position: absolute; left: 0; right: 0; top: 312px;
    text-align: center;
    font-family: "Jost", sans-serif; font-weight: 600; font-size: 20px;
    letter-spacing: .3px;
  }
  .card--front .tagline { color: var(--bright-green); }
  .card--back .tagline { color: var(--lemon); }

  /* Front: brand + services */
  .brand {
    position: absolute; left: 34px; top: 150px; width: 290px;
    display: flex; align-items: center; gap: 14px;
  }
  .brand__dot {
    flex: none; width: 30px; height: 30px; border-radius: 50%;
    background: var(--leaf-green);
  }
  .brand__name {
    font-family: "Jost", sans-serif; font-weight: 700;
    color: var(--leaf-green); text-transform: uppercase;
    line-height: 1.05;
  }
  .brand__name .line1 { display: block; font-size: 33px; letter-spacing: .5px; }
  .brand__name .line2 { display: block; font-size: 16px; letter-spacing: 3px; }

  .services {
    position: absolute; top: 134px; list-style: none;
    font-family: "Jost", sans-serif; font-weight: 600; font-size: 15px;
    line-height: 24.5px; letter-spacing: .3px;
  }
  .services--left { right: 250px; text-align: right; color: var(--bright-green); }
  .services--right { left: 528px; color: var(--lemon); }
  .services li::before { content: "- "; }
  .services .service--extra { color: var(--lemon); }

  /* Back: owner + contacts */
  .owner {
    position: absolute; left: 40px; top: 168px; width: 350px;
    font-family: "Quicksand", sans-serif; font-weight: 700;
    color: var(--lemon); font-size: 28px; line-height: 30px;
    letter-spacing: 1px;
    text-shadow: 0 0 6px rgba(230,234,31,.75), 0 0 14px rgba(230,234,31,.4);
  }
  .owner__name { display: block; text-align: center; }
  .owner__role { display: block; padding-left: 112px; }

  .divider {
    position: absolute; left: 416px; top: 128px; width: 2px; height: 140px;
    background: linear-gradient(180deg, transparent, #3c3d3a 20%, #3c3d3a 80%, transparent);
  }

  .contacts {
    position: absolute; left: 446px; top: 119px; list-style: none;
    font-family: "Quicksand", sans-serif; font-weight: 700;
    font-size: 16.5px; line-height: 22px;
    color: var(--bright-green);
  }
</style>
</head>
<body>
<main class="sheet">

  <section class="card card--front" aria-label="Card front">
    <div class="card__band"></div>

    <div class="brand">
      <span class="brand__dot"></span>
      <p class="brand__name"><span class="line1">Hollowbrook</span><span class="line2">Yard Services</span></p>
    </div>

    <ul class="services services--left">
      <li>Gardening</li>
      <li>Lawn Care</li>
      <li>Hedge Trimming</li>
      <li>Rubbish Removal</li>
      <li>Weeding/Spraying</li>
      <li>Landscaping</li>
    </ul>
    <ul class="services services--right">
      <li>Gutter Cleaning</li>
      <li>Solar Panel Cleaning</li>
      <li>Irrigation</li>
      <li>Pruning</li>
      <li>On-Site Mulching</li>
      <li class="service--extra">Ask for other services</li>
    </ul>

    <p class="tagline">What can Hollowbrook do for you?</p>
  </section>

  <section class="card card--back" aria-label="Card back">
    <div class="card__band"></div>

    <p class="owner">
      <span class="owner__name">Miles Fenwarick</span>
      <span class="owner__role">Owner</span>
    </p>

    <span class="divider"></span>

    <ul class="contacts">
      <li>Ph: 1300 555 014</li>
      <li>Mob: 0400 555 286</li>
      <li>miles@hollowbrookyard.com.au</li>
      <li>www.hollowbrookyard.com.au</li>
      <li>facebook.com/HollowbrookYard</li>
      <li>twitter.com/HollowbrookYard</li>
      <li>ABN: 555 019 472</li>
    </ul>

    <p class="tagline">What can Hollowbrook do for you?</p>
  </section>

</main>
</body>
</html>
```